Letter and Envelope Design For Larchmont Realty

Please design a letter and an envelope incorporating our logo (See Attached). We are also launched a business card contest. Since we want them to match, please feel free to submit a design for both the business card and also the letter design and envelope.

Requirements
Must have
• The envelope, the letter and the business cards must match somehow connecting the designs. We want them to have something that holds them together besides the logo.

```html
<!DOCTYPE html>
<html lang="en">
<head>
<meta charset="utf-8">
<title>Larchmont Realty Stationery</title>
<link href="https://fonts.googleapis.com/css2?family=Lato:wght@400;700&display=swap" rel="stylesheet">
<style>
:root{
  --navy:#2b2f7e;
  --grey:#58585a;
  --text:#4a4a4c;
  --stage:#dcdddf;
  --paper:#ffffff;
}
*{margin:0;padding:0;box-sizing:border-box}
html,body{width:1200px;height:728px;overflow:hidden;background:var(--stage);font-family:'Lato',sans-serif;color:var(--text)}
.canvas{position:relative;width:1200px;height:728px}
.sheet{position:absolute;background:var(--paper);box-shadow:0 1px 4px rgba(0,0,0,.18)}
.accent-bar{position:absolute;left:0;right:0;bottom:0;display:flex}
.accent-bar span{flex:1}
.accent-bar .navy{background:var(--navy)}
.accent-bar .grey{background:var(--grey)}
.brand{position:absolute;display:flex;flex-direction:column;align-items:center;transform:translateX(-50%);text-align:center}
.brand-ring{border:2px solid var(--navy);border-radius:50%}
.brand-name{color:var(--navy);font-weight:700;letter-spacing:.12em;line-height:1.15;white-space:nowrap}

.letterhead{left:26px;top:26px;width:523px;height:677px}
.letterhead .brand{left:261px;top:24px}
.letterhead .brand-ring{width:50px;height:50px}
.letterhead .brand-name{font-size:15px;margin-top:8px}
.letterhead .accent-bar{height:4px}
.letter-footer{position:absolute;left:0;right:0;bottom:13px;display:flex;justify-content:center;align-items:center;gap:13px;font-size:7.6px;font-weight:700}
.contact-item{display:flex;align-items:center;gap:3px}
.icon{width:11px;height:11px;flex:none}

.envelope{left:574px;top:90px;width:601px;height:261px}
.envelope .brand{left:63px;top:13px}
.envelope .brand-ring{width:40px;height:40px}
.envelope .brand-name{font-size:11.5px;margin-top:6px}
.return-address{position:absolute;left:63px;top:82px;transform:translateX(-50%);font-size:6px;font-weight:700;text-align:center;line-height:1.5;white-space:nowrap}
.envelope .accent-bar{height:5px}

.card{top:377px;width:122px;height:215px}
.card .accent-bar{height:5px}
.card-front{left:746px}
.card-front .brand{left:61px;top:77px}
.card-front .brand-ring{width:32px;height:32px}
.card-front .brand-name{font-size:9.5px;margin-top:5px}
.card-back{left:881px;text-align:center}
.holder-name{position:absolute;left:0;right:0;top:52px;color:var(--navy);font-weight:700;font-size:8px}
.holder-title{position:absolute;left:0;right:0;top:64px;font-size:5.6px}
.divider{position:absolute;left:49px;top:87px;width:25px;height:1px;background:var(--navy)}
.card-address{position:absolute;left:0;right:0;top:99px;font-size:5.6px;font-weight:700;line-height:1.55}
.card-icons{position:absolute;left:0;right:0;top:127px;display:flex;justify-content:center;gap:2px}
.card-icons .icon{width:9px;height:9px}
.card-contacts{position:absolute;left:0;right:0;top:140px;font-size:5.6px;font-weight:700;line-height:1.6}
</style>
</head>
<body>
<div class="canvas">

  <svg width="0" height="0" style="position:absolute">
    <defs>
      <symbol id="i-phone" viewBox="0 0 12 12"><circle cx="6" cy="6" r="5.3" fill="none" stroke="#2b2f7e" stroke-width="1"/><path d="M4 3.3l1 .1.5 1.4-.7.6c.4.9 1 1.5 1.9 1.9l.6-.7 1.4.5.1 1c-.2.5-.7.7-1.2.6C5.6 8.3 3.7 6.4 3.4 4.5c-.1-.5.1-1 .6-1.2z" fill="#4a4a4c"/></symbol>
      <symbol id="i-mail" viewBox="0 0 12 12"><circle cx="6" cy="6" r="5.3" fill="none" stroke="#2b2f7e" stroke-width="1"/><rect x="3.3" y="4" width="5.4" height="4" fill="none" stroke="#4a4a4c" stroke-width=".8"/><path d="M3.3 4l2.7 2 2.7-2" fill="none" stroke="#4a4a4c" stroke-width=".8"/></symbol>
      <symbol id="i-web" viewBox="0 0 12 12"><circle cx="6" cy="6" r="5.3" fill="none" stroke="#2b2f7e" stroke-width="1"/><circle cx="6" cy="6" r="3" fill="none" stroke="#4a4a4c" stroke-width=".7"/><ellipse cx="6" cy="6" rx="1.2" ry="3" fill="none" stroke="#4a4a4c" stroke-width=".7"/><path d="M3 6h6" stroke="#4a4a4c" stroke-width=".7"/></symbol>
    </defs>
  </svg>

  <section class="sheet letterhead">
    <div class="brand">
      <div class="brand-ring"></div>
      <div class="brand-name">LARCHMONT REALTY</div>
    </div>
    <footer class="letter-footer">
      <span>48 Birchwood Lane Suite 300, Larchmont, NY 10538</span>
      <span class="contact-item"><svg class="icon"><use href="#i-phone"/></svg>555.014.2290</span>
      <span class="contact-item"><svg class="icon"><use href="#i-mail"/></svg>info@larchrealty.com</span>
      <span class="contact-item"><svg class="icon"><use href="#i-web"/></svg>www.larchrealty.com</span>
    </footer>
    <div class="accent-bar"><span class="navy"></span><span class="grey"></span></div>
  </section>

  <section class="sheet envelope">
    <div class="brand">
      <div class="brand-ring"></div>
      <div class="brand-name">LARCHMONT REALTY</div>
    </div>
    <address class="return-address" style="font-style:normal">48 Birchwood Lane Suite 300<br>Larchmont, NY 10538</address>
    <div class="accent-bar"><span class="navy"></span><span class="grey"></span></div>
  </section>

  <section class="sheet card card-front">
    <div class="brand">
      <div class="brand-ring"></div>
      <div class="brand-name">LARCHMONT REALTY</div>
    </div>
    <div class="accent-bar"><span class="navy"></span><span class="grey"></span></div>
  </section>

  <section class="sheet card card-back">
    <div class="holder-name">DANIEL MOREAU</div>
    <div class="holder-title">Managing Member, Founder</div>
    <div class="divider"></div>
    <div class="card-address">48 Birchwood Lane Suite 300<br>Larchmont, NY 10538</div>
    <div class="card-icons">
      <svg class="icon"><use href="#i-phone"/></svg>
      <svg class="icon"><use href="#i-mail"/></svg>
      <svg class="icon"><use href="#i-web"/></svg>
    </div>
    <div class="card-contacts">555.014.2290<br>daniel@larchrealty.com<br>www.larchrealty.com</div>
    <div class="accent-bar"><span class="navy"></span><span class="grey"></span></div>
  </section>

</div>
</body>
</html>
```